Employee I.D. Card - Badge

We need an employee I.D. card designed. Our employees are going to be wearing these. I would like to have it look nice. Something professional yet cool (not uptight if that makes sense).
Project Scope:
Vertical orientation
Company name ------------- (Bright and Tidy)
Website ------------- (brightandtidymn.example)
Employee Picture
background check image
front and back designed - same design on either side
You can create the card without having the employee images on them.
Here are the dimensions -
2.125 x 3.370 inches
Double sided - same design can be used front and back
Background badge - I would like to add an image that shows that the employee has taken a background check. I've added the press-kit for the company we use. If you have a better idea than incorporating their logo, we can certainly do something different.
Example image-
https://www.findwell-search.example/results?q=background+check+badge&mode=images
The print company will set up the names.
Logo is attached
Also attached are our business cards. You can use this for an idea of brand/company style.
Our website - brightandtidymn.example

```html
<!DOCTYPE html>
<html lang="en">
<head>
<meta charset="utf-8">
<title>Bright and Tidy – Employee ID Badge</title>
<link rel="stylesheet" href="https://fonts.googleapis.com/css2?family=Questrial&display=swap">
<style>
  :root {
    --canvas: #ffffff;
    --card-edge: #d4d4d4;
    --brand-blue: #1b82cc;
    --brand-green: #9cc31f;
    --text-grey: #8e8e8e;
    --photo-grey: #c6c7c7;
    --rule: #b9b9b9;
    --ink: #2a2a2a;
  }
  * { box-sizing: border-box; margin: 0; padding: 0; }
  html, body {
    width: 1200px; height: 1200px; overflow: hidden;
    background: var(--canvas);
    font-family: "Questrial", "Helvetica Neue", Arial, sans-serif;
  }
  .canvas { position: relative; width: 1200px; height: 1200px; }
  .badge-card {
    position: absolute; left: 325px; top: 164px;
    width: 550px; height: 871px;
    border: 1px solid var(--card-edge);
    background: #fff;
  }
  .brand {
    position: absolute; left: 0; right: 0; top: 92px;
    display: flex; justify-content: center; align-items: flex-start; gap: 14px;
  }
  .brand-dot {
    width: 22px; height: 22px; border-radius: 50%;
    background: var(--brand-blue); margin-top: 14px;
  }
  .brand-name {
    color: var(--brand-blue);
    font-size: 88px; line-height: 0.98; letter-spacing: -2px;
    text-align: left;
  }
  .brand-url {
    position: absolute; left: 0; right: 0; top: 312px;
    padding-left: 100px;
    text-align: center; color: var(--text-grey); font-size: 19px;
  }
  .portrait {
    position: absolute; left: 131px; top: 410px;
    width: 288px; height: 288px;
  }
  .portrait svg { overflow: visible; }
  .employee-name {
    position: absolute; left: 0; right: 0; top: 708px;
    text-align: center; color: var(--brand-green); font-size: 42px;
  }
  .divider {
    position: absolute; left: 209px; top: 778px;
    width: 132px; height: 1px; background: var(--rule);
  }
  .screening-partner {
    position: absolute; left: 0; right: 0; top: 802px;
    display: flex; justify-content: center; align-items: center; gap: 6px;
  }
  .partner-name { color: var(--ink); font-size: 19px; }
  .partner-dot {
    width: 20px; height: 20px; border-radius: 50%; background: var(--brand-green);
  }
</style>
</head>
<body>
<main class="canvas">
  <section class="badge-card">
    <header class="brand">
      <span class="brand-dot"></span>
      <h1 class="brand-name">Bright<br>and Tidy</h1>
    </header>
    <p class="brand-url">brightandtidymn.example</p>

    <div class="portrait">
      <svg width="288" height="288" viewBox="0 0 288 288">
        <circle cx="144" cy="144" r="143" fill="#fff" stroke="var(--brand-green)" stroke-width="1.5"/>
        <circle cx="144" cy="150" r="136" fill="var(--photo-grey)" role="img" aria-label="Employee photo placeholder"/>
        <path d="M 33 230 A 142 142 0 0 0 255 230" fill="none" stroke="var(--brand-green)" stroke-width="3"/>
        <circle cx="249" cy="230" r="48" fill="var(--brand-blue)" stroke="#fff" stroke-width="3" role="img" aria-label="Background check cleared seal"/>
      </svg>
    </div>

    <h2 class="employee-name">Alex Moreno</h2>
    <div class="divider"></div>
    <footer class="screening-partner">
      <span class="partner-name">VettaCheck</span>
      <span class="partner-dot"></span>
    </footer>
  </section>
</main>
</body>
</html>
```